pathology learning flashcard template graphic design .

Creative designs for 2 sides of the flashcards to include colorful sectioning and font sizes that will make it easy to use in studying.

```html
<!DOCTYPE html>
<html lang="en">
<head>
<meta charset="utf-8">
<title>Pathology Flashcard – Achalasia</title>
<link href="https://fonts.googleapis.com/css2?family=Ultra&family=Questrial&family=Fira+Sans+Condensed:wght@600&family=Open+Sans:ital@1&display=swap" rel="stylesheet">
<style>
  :root{
    --red:#a3070b;
    --gold:#e3a500;
    --teal:#2fb8aa;
    --orange:#ff6a1f;
    --ink:#1c1c1c;
    --paper:#ffffff;
  }
  *{box-sizing:border-box;margin:0;padding:0}
  html,body{width:899px;height:1200px;overflow:hidden;background:var(--paper)}
  body{position:relative;font-family:"Questrial",sans-serif;color:var(--ink)}
  .abs{position:absolute}

  /* ---------- front side ---------- */
  .card{position:absolute;left:33px;width:830px;border:1px solid #222;background:var(--paper)}
  .card--front{top:17px;height:570px}
  .card--back{top:606px;height:570px}

  .front-band{position:absolute;left:0;top:0;width:100%;height:79px;background:var(--gold);
    display:flex;align-items:center;justify-content:center}
  .front-title{font-family:"Ultra",serif;color:var(--red);font-size:49px;letter-spacing:1px;line-height:1}

  .case-id{left:35px;top:110px;font-size:27px;color:var(--red);letter-spacing:-0.3px}

  .stripe{position:absolute;left:759px;width:71px;height:18px}
  .stripe--red{top:95px;background:var(--red)}
  .stripe--teal{top:119px;background:var(--teal)}
  .stripe--gold{top:143px;background:var(--gold)}
  .stripe--orange{top:165px;background:var(--orange)}

  .question-frame{left:15px;top:154px;width:800px;height:400px;border:5px solid var(--red);border-radius:30px}
  .question-divider{position:absolute;left:0;right:0;top:295px;height:5px;background:var(--red)}
  .question-text{left:15px;top:17px;width:760px;font-size:21.3px;line-height:28.8px;color:#333}

  .option{position:absolute;font-size:22px;color:#333;display:flex;align-items:baseline;gap:10px}
  .option b{font-family:"Fira Sans Condensed",sans-serif;color:var(--red);font-size:22px}

  /* ---------- back side ---------- */
  .topic{left:20px;top:12px;font-family:"Ultra",serif;font-size:40px;color:var(--red);line-height:1}

  .panel{position:absolute;border-style:solid;border-width:5px;border-radius:17px;background:var(--paper)}
  .panel--definition{left:13px;top:60px;width:345px;height:137px;border-color:var(--red)}
  .panel--etiology{left:13px;top:212px;width:345px;height:138px;border-color:var(--teal)}
  .panel--findings{left:370px;top:11px;width:445px;height:339px;border-color:var(--orange)}

  .tab{position:absolute;left:1px;top:1px;background:var(--paper);border-style:solid;border-width:0 4px 4px 0;padding:0 5px;line-height:1}
  .tab--definition{border-color:var(--red);color:var(--red);font-size:18px;height:27px;padding-top:4px}
  .tab--etiology{border-color:var(--teal);color:var(--teal);font-size:19px;height:28px;padding-top:4px}
  .tab--findings{border-color:var(--orange);color:var(--red);font-family:"Fira Sans Condensed",sans-serif;font-size:22px;height:38px;padding:7px 10px 0 12px;letter-spacing:-0.5px}

  .panel-text{position:absolute;font-size:12.6px;line-height:18px;color:#222}
  .panel--definition .panel-text{left:8px;top:42px;width:320px}
  .panel--etiology .panel-text{left:9px;top:43px;width:320px}
  .panel--findings .panel-text{left:14px;top:58px;width:415px}
  .panel-text p{margin-bottom:9px}
  .label{color:#e84810;font-size:15px}

  .answer{position:absolute;left:13px;top:364px;width:802px;height:170px;background:var(--gold);border-radius:15px;padding:12px 16px}
  .answer-title{font-size:21px;color:var(--red);display:flex;gap:6px;align-items:baseline;margin-bottom:3px}
  .answer-title b{font-family:"Fira Sans Condensed",sans-serif}
  .answer-text{font-size:14.6px;line-height:20.3px;color:#fff6e6}

  .sources{left:13px;top:550px;font-family:"Open Sans",sans-serif;font-style:italic;font-size:8.6px;color:#111}
  .page-number{left:775px;top:542px;font-size:17px;font-style:italic;color:#111}
</style>
</head>
<body>

<section class="card card--front">
  <header class="front-band"><h1 class="front-title">GASTROINTESTINAL</h1></header>
  <h2 class="abs case-id">PATHOLOGY CASE ID 0001</h2>
  <span class="stripe stripe--red"></span>
  <span class="stripe stripe--teal"></span>
  <span class="stripe stripe--gold"></span>
  <span class="stripe stripe--orange"></span>

  <div class="abs question-frame">
    <p class="abs question-text">50-year-old woman comes to the clinic because she has difficulty swallowing for the past few months. She says symptoms have been worsening. She also complains of cough, mostly at night and in fear of choking, has stopped eating many foods, losing about 12 lbs in the past 3 months. Past medical history is unremarkable. Vital signs are normal and physical exam is unremarkable. Chest x-ray with demonstrates an air-fluid level, while manometry shows absent relaxation of the lower esophageal sphincter during swallowing. What is the most likely diagnosis?</p>
    <div class="question-divider"></div>
    <div class="option" style="left:129px;top:312px"><b>A)</b> GERD</div>
    <div class="option" style="left:427px;top:312px"><b>B)</b> Barret Esophagus</div>
    <div class="option" style="left:129px;top:352px"><b>C)</b> Achalasia</div>
    <div class="option" style="left:427px;top:352px"><b>D)</b> Eosinophilic esophagitis</div>
  </div>
</section>

<section class="card card--back">
  <h2 class="abs topic">Achalasia</h2>

  <div class="panel panel--definition">
    <span class="tab tab--definition">Definition</span>
    <div class="panel-text">&nbsp;•Motility disorder where esophageal relaxation is impaired in the lower esophageal sphincter (LES).</div>
  </div>

  <div class="panel panel--etiology">
    <span class="tab tab--etiology">Etiology/Pathology</span>
    <div class="panel-text">Destruction of inhibitory neurons in the Auerbach plexus. Loss of peristalsis in the lower esophageal sphincter (Lower-two thirds of the esophagus).</div>
  </div>

  <div class="panel panel--findings">
    <span class="tab tab--findings">P/E and Symptoms</span>
    <div class="panel-text">
      <p>&nbsp;•Dysphagia that is progressive, regurgitation, weight-loss, dry cough, chest pain, GERD, esophageal perforation, squamous cell carcinoma, aspiration pneumonia.</p>
      <p><span class="label">Dx:</span> •Barium swallow will show ‘bird’s beak’ and esophageal dilation. Manometry will present with increased resting lower esophageal sphincter pressure. Endoscopy will usually present with normal mucosa and LES dilation, and in some cases residual material such as undigested food particles may be present.</p>
      <p><span class="label">Rx:</span> First line of treatment are nitrates, calcium channel blockers, and Botulinum toxin injection in the LES. Long term management options include esophageal dilation with pneumatic balloon and myotomy.</p>
    </div>
  </div>

  <div class="answer">
    <div class="answer-title"><b>C)</b> Achalasia</div>
    <p class="answer-text">Symptoms and studies suggestive of achalasia. Patient’s manometry presents with no relaxation of the lower esophageal sphincter during swallowing. Patient also complains of dysphagia and is unable to swallow properly, leading to weight loss. Patient has no past infection or inflammation, ruling out eosinophilic esophagitis. Patient does not have chronic GERD, eliminating the possibility of Barrett esophagus, in which at least 5 years of acid reflux are beforehand to develop columnar metaplasia.</p>
  </div>

  <p class="abs sources">Sources:Harlow’s Drug guide;Pennfield pocket Formulary;Medlisto.com;Clinoscope.com</p>
  <span class="abs page-number">1</span>
</section>

</body>
</html>
```